Mail - Scan, Sort & Forward - Web Design

We need a web design for a mail scan, store, view and forward service. It is a lifestyle service predicated on freedom, convenience, ease of access, ease of use, security, safety. It involves personal information and is accessed remotely.
No branding or style guide is yet complete so an open pallet is available but design should convey simplicity as it targets demographic 45-75 years travellers but also high net worth multi location professionals, miners and other multi-location workers.
Competitor sites are: (for business description examples)
www.brindlecrate.example
www.tovelmarsh.example.au
www.quillorbenhaven.example.au
Updates

Attached files are wireframes which show how the service will work (UI). You should use these to form ideas about your web design for the service. They are not templates nor am I looking for a UI dev (yet).

Target Market(s)

Travellers ( especially retirees) and multi-location workers eg miners

Industry/Entity Type

Business

Requirements
Must have
• Being a lifestyle site, the pages must be low on text, lite layout, imagery addressing the target market.
Navigation should be simple to use
Concept of visitor / member / client should be addressed. The user needs to be able to permission other user groups (read-only)
Talk to reasons why prospects want to use this service.
Nice to have
• access to view nearest Kerrin Dispatch office.
Regular call to action like survey, quiz or did you know info which may keep the user returning to the site.
Campaign section which enables customising of campaigns on an ongoing basis
Ability to access and download Terms & conditions, brochures .pdf or other information.
Simulate how service works..video or webcast
Should not have
• Do not want heavy or dense text everywhere. Use imagery where possible. Icons should be thematic not isolated.

```html
<!DOCTYPE html>
<html lang="en">
<head>
<meta charset="utf-8">
<title>ParcelNook.au – New Postal Mail</title>
<link href="https://fonts.googleapis.com/css2?family=Arimo:wght@400;700&display=swap" rel="stylesheet">
<style>
:root{
  --ink:#333;
  --muted:#555;
  --orange:#e8750c;
  --orange-dark:#7a3100;
  --bar:#2b2b2b;
  --page:#fff;
  --table-bg:#ebebeb;
  --table-line:#bdbdbd;
  --teal:#1c6f86;
  --sky:#22a7dc;
  --green:#8cc51a;
  --green-dark:#5e9a0c;
  --footer:#1e1e1e;
}
*{box-sizing:border-box;margin:0;padding:0}
html,body{width:1085px;height:1200px;overflow:hidden;background:var(--page)}
body{font-family:"Arimo",Arial,sans-serif;color:var(--ink)}
.page{position:relative;width:1000px;height:1106px;transform:scale(1.085);transform-origin:0 0;background:#fff}
.abs{position:absolute}

.site-header{left:0;top:0;width:1000px;height:92px;background:linear-gradient(#fff,#f2f2f2)}
.brand{left:38px;top:30px;font-size:30px;font-weight:700;color:var(--orange);letter-spacing:-.5px}
.search{left:720px;top:33px;width:202px;height:25px;border-radius:5px;background:linear-gradient(#cfcfcf,#e0e0e0);border:1px solid #bbb;font-size:11px;font-style:italic;color:#888;padding:6px 12px}
.search-icon{left:928px;top:35px}

.util-bar{left:0;top:92px;width:1000px;height:38px;background:linear-gradient(#3a3a3a,#222);color:#fff;font-size:13px}
.util-bar .lang{left:778px;top:12px}
.util-bar .flag{left:752px;top:13px;width:18px;height:12px;background:#1f3b8a;border:1px solid #fff}
.util-bar .login{left:884px;top:12px}
.util-bar .lock{left:865px;top:11px}

.main-nav{left:0;top:130px;width:1000px;height:52px;background:linear-gradient(#f28a1c 0%,#e06f08 45%,#8a3a02 100%)}
.main-nav ul{list-style:none;display:flex;gap:0;position:absolute;left:38px;top:16px}
.main-nav li{color:#fff;font-weight:700;font-size:15px;margin-right:31px}
.nav-shadow{left:0;top:182px;width:1000px;height:12px;background:#2a2a2a}
.nav-pointer{left:48px;top:194px}

.page-title{left:38px;top:223px;font-size:17px;font-weight:700;color:#333}
.title-icon{left:215px;top:215px}

.hero{left:35px;top:258px;width:924px;height:140px;border:3px solid #dcdcdc;border-radius:6px;background:linear-gradient(90deg,#d9c4b5 0%,#f4f4f4 20%,#e9eef3 45%,#f7f7f7 65%,#e8dcb8 80%,#f3f3f3 100%)}

.tabs{left:13px;top:414px;display:flex;gap:18px}
.tab{width:180px;height:42px;border-radius:5px;background:linear-gradient(#5a5a5a,#1e1e1e);color:#fff;font-size:15px;display:flex;align-items:center;justify-content:center;box-shadow:0 2px 2px rgba(0,0,0,.35)}

.mail-table{left:23px;top:479px;width:757px;height:224px;border:1px solid var(--table-line);border-radius:6px;background:var(--table-bg);overflow:hidden}
.mail-table .head{position:absolute;left:0;top:0;width:100%;height:41px;background:linear-gradient(#f5f5f5,#cfcfcf);border-bottom:1px solid #b0b0b0}
.col-sep{position:absolute;top:0;width:1px;height:41px;background:#aaa}
.th{position:absolute;top:13px;font-size:15px;color:#555}
.td{position:absolute;font-size:12.5px;color:#444}
.check{position:absolute;width:11px;height:11px;border:1px solid #888;background:#fff;border-radius:2px}

.survey{left:804px;top:478px;width:182px;height:190px;border:1px solid #c5dde4;border-radius:4px;background:linear-gradient(#fff 0%,#cbe7ef 100%)}
.survey h3{position:absolute;left:43px;top:16px;font-size:14px;color:var(--teal)}
.survey .opt{position:absolute;left:44px;font-size:12.5px;color:var(--teal)}
.survey .radio{position:absolute;left:25px;width:10px;height:10px;border-radius:50%;border:1px solid #777;background:#fff}
.survey .submit{position:absolute;left:60px;top:161px;width:62px;height:20px;border-radius:10px;background:linear-gradient(#fff,#cfcfcf);border:1px solid #999;font-size:12px;text-align:center;line-height:18px;color:#444}

.promo{left:805px;top:678px;width:182px;height:123px;border-radius:4px;background:linear-gradient(#55cdf3,#1aa0dc);color:#fff}
.promo .envelope{position:absolute;left:12px;top:10px;width:44px;height:40px;border-radius:4px;background:linear-gradient(#ffd36a,#e8a318)}
.promo .t1{position:absolute;left:68px;top:10px;font-size:16px;font-weight:700}
.promo .t2{position:absolute;left:68px;top:30px;font-size:22px;font-weight:700}
.promo .t3{position:absolute;left:18px;top:62px;font-size:9.5px;line-height:16px}
.promo .btn{position:absolute;left:90px;top:92px;width:70px;height:22px;border-radius:4px;background:linear-gradient(#c8f04a,#7dbb12);border:1px solid #fff;color:#1f3d05;font-size:11.5px;font-weight:700;text-align:center;line-height:20px}

.cta{top:724px;width:289px;height:67px;border-radius:3px;background:linear-gradient(#a9d84a 0%,#8cc51a 50%,#6eae0e 51%,#8cc51a 100%);color:#fff;font-weight:700}
.cta .icon{position:absolute;left:14px;top:10px;width:46px;height:46px;border-radius:6px;background:linear-gradient(#d83a3a,#9e1010)}
.cta .line1{position:absolute;left:80px;width:200px;text-align:center;top:10px;font-size:16px;color:#2e5a05}
.cta .line2{position:absolute;left:80px;width:200px;text-align:center;top:39px;font-size:17px}
.cta-terms{left:62px}
.cta-call{left:404px}

.video{left:58px;top:830px;width:225px;height:152px;border:3px solid #e2e2e2;border-radius:6px;background:#fff;overflow:hidden}
.video .frame{position:absolute;left:0;top:0;width:100%;height:136px;background:radial-gradient(ellipse at 45% 55%,#b7c7d4 0%,#eef2f5 45%,#fff 75%)}
.video .play{position:absolute;left:94px;top:58px;width:32px;height:32px;border-radius:50%;background:rgba(60,60,60,.75)}
.video .controls{position:absolute;left:0;bottom:0;width:100%;height:13px;background:#d6d6d6;border-top:1px solid #aaa}
.video .track{position:absolute;left:18px;top:5px;width:140px;height:3px;background:#888}
.video .time{position:absolute;left:166px;top:1px;font-size:7px;color:#333}

.intro{left:305px;top:843px;width:647px}
.intro h2{font-size:14.5px;margin-bottom:18px}
.intro p{font-size:12px;line-height:24px;text-align:justify;color:#333}

.site-footer{left:0;top:1009px;width:1000px;height:97px;background:var(--footer);color:#ddd;font-size:11.5px}
.site-footer ul{list-style:none;display:flex;position:absolute;left:47px;top:28px}
.site-footer li{margin-right:25px}
.site-footer .copy{position:absolute;left:47px;top:59px}
.site-footer .connect{position:absolute;left:667px;top:28px}
.social{position:absolute;top:22px;width:24px;height:24px;border-radius:50%;background:#555}
</style>
</head>
<body>
<div class="page">

  <header class="site-header abs">
    <div class="brand abs">ParcelNook.au</div>
    <div class="search abs">Search...</div>
    <svg class="search-icon abs" width="20" height="20" viewBox="0 0 20 20"><circle cx="8" cy="8" r="6" fill="none" stroke="#aaa" stroke-width="2"/><line x1="12.5" y1="12.5" x2="18" y2="18" stroke="#aaa" stroke-width="2.5"/></svg>
  </header>

  <div class="util-bar abs">
    <div class="flag abs"></div>
    <span class="lang abs">English</span>
    <svg class="lock abs" width="12" height="14" viewBox="0 0 12 14"><path d="M3 6V4a3 3 0 0 1 6 0v2" fill="none" stroke="#fff" stroke-width="1.5"/><rect x="1" y="6" width="10" height="8" rx="1" fill="#fff"/></svg>
    <span class="login abs">Log in</span>
  </div>

  <nav class="main-nav abs">
    <ul><li>Home</li><li>About Us</li><li>Services</li><li>Pricing</li><li>FAQ's</li><li>Contact Us</li><li>Log in</li></ul>
  </nav>
  <div class="nav-shadow abs"></div>
  <svg class="nav-pointer abs" width="20" height="9" viewBox="0 0 20 9"><polygon points="0,0 20,0 10,9" fill="#2a2a2a"/></svg>

  <h1 class="page-title abs">New Postal Mail Page</h1>
  <svg class="title-icon abs" width="34" height="32" viewBox="0 0 34 32"><polygon points="3,14 17,3 31,14 31,29 3,29" fill="#c8c8c8"/><polygon points="3,14 17,22 31,14 31,29 3,29" fill="#9b9b9b"/><rect x="8" y="8" width="18" height="11" fill="#f3f3f3"/></svg>

  <div class="hero abs" role="img" aria-label="Banner photo: smiling woman beside a laptop and stacks of paper mail turning into PDF files"></div>

  <div class="tabs abs">
    <div class="tab">New Postal Mail</div>
    <div class="tab">Archive Postal Mail</div>
    <div class="tab">Document Vault</div>
    <div class="tab">User Profile &amp; Access</div>
    <div class="tab">Account History</div>
  </div>

  <section class="mail-table abs">
    <div class="head">
      <span class="check" style="left:15px;top:14px"></span>
      <span class="th" style="left:47px">Data Recd</span>
      <span class="col-sep" style="left:140px"></span>
      <span class="th" style="left:163px">Document Type</span>
      <span class="col-sep" style="left:287px"></span>
      <span class="th" style="left:313px">Scan/Not Scan</span>
      <span class="col-sep" style="left:434px"></span>
      <span class="th" style="left:457px">Document Name</span>
      <span class="col-sep" style="left:585px"></span>
      <span class="th" style="left:612px">Sender</span>
    </div>
    <span class="check" style="left:15px;top:59px"></span>
    <span class="td" style="left:47px;top:57px">Date Recd</span>
    <span class="td" style="left:163px;top:57px">Document Type</span>
    <span class="td" style="left:313px;top:57px">Scanned/Not Scan</span>
    <span class="td" style="left:458px;top:57px">Document Name</span>
    <span class="td" style="left:612px;top:57px">Supplier Name</span>

    <span class="td" style="left:47px;top:87px">25 Feb 2011</span>
    <span class="td" style="left:163px;top:87px">Invoice</span>
    <span class="td" style="left:313px;top:87px">Scanned</span>
    <span class="td" style="left:612px;top:87px">Ferrow - Gas</span>

    <span class="td" style="left:163px;top:117px">‘Restricted’</span>
    <span class="td" style="left:313px;top:117px">Client Request</span>
    <span class="td" style="left:612px;top:117px">Letter fm Aunty Joan</span>

    <span class="td" style="left:163px;top:147px">Prospectus</span>
    <span class="td" style="left:313px;top:147px;line-height:20px">Too large/ Not<br>Scanned</span>
    <span class="td" style="left:612px;top:147px">Brantor</span>
  </section>

  <aside class="survey abs">
    <svg style="position:absolute;left:9px;top:12px" width="28" height="22" viewBox="0 0 28 22"><polyline points="3,11 10,18 25,3" fill="none" stroke="#4caa1a" stroke-width="5" stroke-linecap="round" stroke-linejoin="round"/></svg>
    <h3>Online Servey</h3>
    <span class="radio" style="top:48px"></span><span class="opt" style="top:46px">Supplier Name</span>
    <span class="radio" style="top:78px"></span><span class="opt" style="top:76px">Ferrow - Gas</span>
    <span class="radio" style="top:108px"></span><span class="opt" style="top:106px">Letter fm Aunty Joan</span>
    <span class="radio" style="top:138px"></span><span class="opt" style="top:136px">Brantor</span>
    <div class="submit">Submit</div>
  </aside>

  <aside class="promo abs">
    <div class="envelope" role="img" aria-label="Golden envelope illustration"></div>
    <div class="t1">Postal Mail</div>
    <div class="t2">Scan</div>
    <div class="t3">Lorem Ipsum Contantry Popular<br>Dummy text</div>
    <div class="btn">Click Here</div>
  </aside>

  <a class="cta cta-terms abs">
    <span class="icon"></span>
    <span class="line1">Terms and Conditions</span>
    <span class="line2">Download as PDF</span>
  </a>
  <a class="cta cta-call abs">
    <span class="icon"></span>
    <svg style="position:absolute;left:25px;top:21px" width="24" height="24" viewBox="0 0 24 24"><path d="M5 2h4l2 5-3 2a12 12 0 0 0 7 7l2-3 5 2v4a2 2 0 0 1-2 2A19 19 0 0 1 3 4a2 2 0 0 1 2-2z" fill="#fff"/></svg>
    <span class="line1">Call To Action</span>
    <span class="line2">we are ready to help you</span>
  </a>

  <div class="video abs">
    <div class="frame" role="img" aria-label="Video still: laptop with paper mail flying into the screen"></div>
    <svg class="play" viewBox="0 0 32 32"><polygon points="12,9 24,16 12,23" fill="#fff"/></svg>
    <div class="controls"><div class="track"></div><span class="time">0:00 / 0:00</span></div>
  </div>

  <section class="intro abs">
    <h2>Lorem Ipsum Contantry</h2>
    <p>It is a long established fact that a reader will be distracted by the readable content of a page when looking at its layout. The point of using Lorem Ipsum is that it has a more-or-less normal distribution of letters, as opposed to using 'Content here, content here', making it look like readable English. Many desktop publishing packages and web page editors now use Lorem Ipsum as their default model text, and a search.</p>
  </section>

  <footer class="site-footer abs">
    <ul><li>Home</li><li>About Us</li><li>Services</li><li>Pricing</li><li>FAQ's</li><li>Contact Us</li><li>Log in</li></ul>
    <div class="copy">Copyright &nbsp;© 2011 www.parcelnook.example.au All rights reserved</div>
    <div class="connect">Connect with us :</div>
    <span class="social" style="left:759px"></span>
    <span class="social" style="left:799px"></span>
    <span class="social" style="left:839px"></span>
    <span class="social" style="left:879px"></span>
    <span class="social" style="left:919px"></span>
  </footer>

</div>
</body>
</html>
```